BRISKET Homes business card Pelmo Press

I've been a Real Estate agent since 1988. I left the BIG brokerages 2 years ago and am on my own and need a business card. I love doing graphics, but don't have the bandwidth right now.

Background. I want a card that stands out like I do. I'm the fun guy that always has a joke or funny story, and my clients like me. Something fun, but not too silly.

I don't have a symbol or logo that I'm using on the card now, but need to include something, a Font by itself or a logo? I'm not sure if we need a logo or not. I'm open.
The GREAT design is going to be the basis for the next project of stationary, note pads, and Real Estate FOR SALE & Open House signs.

Single sided card is fine, but I selected a 2 sided just in case that's what it works out to be.

Here we go. If you need anything else. Please let me know. As I think of anything, I'll add that also.

Target Market(s)

My territory is Santa Clara County / Silicon Valley, CA. I tend to work with new buyers buying a condo ($500,000) up to single family home for about $1.5 million. 1st time buyers and also move-up buyers. I haven't worked with multi-million $$ homes .... but wouldn't turn it down. Clients here tend to be White, Latin and now many more Chinese and East Indians. Clients also tend to be high tech, Zorvat, Quince, Lumigrid workers and also non tech people.

Industry/Entity Type

Business

Contact Information for Business Card

CONTENT:
Company: BRISKET Homes
My name: Harold P. Brisket Jr.
Title: Real Estate Broker
Email: Hal@HaroldBrisket.example
Website: www.HaroldBrisket.example
Phone: (408) 555-0173
BRE # 07395162

Font styles to use
Sans Serif

Requirements
Must have
• Content from above. Something that stands out from the others. Serious enough looking, not stale, maybe a bit fun.

```html
<!DOCTYPE html>
<html lang="en">
<head>
<meta charset="utf-8">
<title>BRISKET Homes – Business Card</title>
<link rel="stylesheet" href="https://fonts.googleapis.com/css2?family=Montserrat:wght@300;400;600&display=swap">
<style>
  :root {
    --canvas-bg: #ecebe9;
    --card-light: #ffffff;
    --card-edge: #d6d6d6;
    --brand-orange: #f0901e;
    --text-grey: #8a8a8a;
    --icon-white: #ffffff;
  }
  * { box-sizing: border-box; margin: 0; padding: 0; }
  html, body {
    width: 1200px; height: 1000px; overflow: hidden;
    background: var(--canvas-bg);
    font-family: "Montserrat", Arial, sans-serif;
  }
  .canvas {
    position: relative; width: 1200px; height: 1000px;
    display: flex; align-items: center; justify-content: center; gap: 40px;
  }
  .card {
    position: relative; width: 540px; height: 309px;
    border-radius: 26px;
    background: radial-gradient(ellipse at 50% 45%, var(--card-light) 0%, #f1f1f1 45%, var(--card-edge) 100%);
    box-shadow: 0 2px 0 #c9c9c9, 0 4px 0 #e2e2e2, 0 6px 0 #c4c4c4, 0 16px 30px rgba(0,0,0,0.18);
    overflow: hidden;
  }
  .wordmark {
    position: absolute;
    color: var(--brand-orange);
    font-weight: 300;
    white-space: nowrap;
  }
  /* Front */
  .card--front .wordmark {
    left: 0; right: 0; top: 140px; text-align: center;
    font-size: 32px; letter-spacing: 3px;
  }
  .licence {
    position: absolute; right: 30px; top: 60px;
    color: var(--brand-orange); font-size: 13px; font-weight: 400; letter-spacing: 0.5px;
  }
  /* Back */
  .card--back .wordmark {
    left: 28px; top: 206px; width: 205px;
    font-size: 22px; letter-spacing: 2px;
  }
  .divider {
    position: absolute; left: 250px; top: 128px; width: 1.5px; height: 116px;
    background: linear-gradient(to bottom, var(--brand-orange), rgba(240,144,30,0.2));
  }
  .agent { position: absolute; right: 60px; top: 32px; text-align: right; }
  .agent__name { color: var(--brand-orange); font-size: 17px; font-weight: 600; }
  .agent__title { color: var(--text-grey); font-size: 12px; font-weight: 400; margin-top: 2px; }
  .contacts { position: absolute; right: 22px; top: 110px; list-style: none; }
  .contacts li {
    display: flex; align-items: center; justify-content: flex-end; gap: 12px;
    height: 30px; margin-bottom: 14px;
    color: var(--brand-orange); font-size: 14px; font-weight: 400;
    white-space: nowrap;
  }
  .contacts svg { width: 26px; height: 28px; flex: none; }
</style>
</head>
<body>
<main class="canvas">
  <section class="card card--front" aria-label="Card front">
    <div class="wordmark">BRISKET Homes</div>
    <div class="licence">BRE # 07395162</div>
  </section>

  <section class="card card--back" aria-label="Card back">
    <div class="wordmark">BRISKET Homes</div>
    <div class="divider"></div>
    <div class="agent">
      <div class="agent__name">Harold P. Brisket Jr.</div>
      <div class="agent__title">Real Estate Broker</div>
    </div>
    <ul class="contacts">
      <li>(408) 555-0173
        <svg viewBox="0 0 26 28" aria-hidden="true">
          <polygon points="13,1 25,7.5 25,20.5 13,27 1,20.5 1,7.5" fill="var(--brand-orange)"/>
          <path d="M9 8 L11.5 8 L12.5 11 L11 12.2 Q12.5 15.5 15.8 17 L17 15.5 L20 16.5 L20 19 Q14 20 10 15 Q7.5 11.5 9 8 Z" fill="var(--icon-white)"/>
        </svg>
      </li>
      <li>Hal@HaroldBrisket.example
        <svg viewBox="0 0 26 28" aria-hidden="true">
          <polygon points="13,1 25,7.5 25,20.5 13,27 1,20.5 1,7.5" fill="var(--brand-orange)"/>
          <rect x="7" y="9.5" width="12" height="9" fill="var(--icon-white)"/>
          <path d="M7 9.5 L13 14.5 L19 9.5" fill="none" stroke="var(--brand-orange)" stroke-width="1.2"/>
        </svg>
      </li>
      <li>www.HaroldBrisket.example
        <svg viewBox="0 0 26 28" aria-hidden="true">
          <polygon points="13,1 25,7.5 25,20.5 13,27 1,20.5 1,7.5" fill="var(--brand-orange)"/>
          <rect x="7.5" y="9" width="11" height="8" fill="none" stroke="var(--icon-white)" stroke-width="1.5"/>
          <rect x="6" y="18" width="14" height="1.8" fill="var(--icon-white)"/>
        </svg>
      </li>
    </ul>
  </section>
</main>
</body>
</html>
```